High-end Oceanfront Real Estate Group Needs Clean, Modern Web Design

I’m looking for a clean, professional, modern and beautiful homepage web design for a Real Estate group in Southern California, USA.

The group/company is “Marlow on the Shore,” and they specialize in high end (i.e. expensive), oceanfront real estate in the Orange County area.

The look and feel of the page should accentuate the brand qualities: luxurious/expensive, professional, and beautiful (Orange County is one of the most beautiful areas in all the US and we would love the site to emphasize the beautiful beaches and scenery it has to offer).

Looks we like:
• www.brantleyhomesrealty.example
• www.keptbyfenwick.example -- I think the design is pretty out-dated in this site, but I like the organization/layout of the site

Header Tags (I don’t know if we can fit all of these, may need a side-menu, but I’d prefer header title only if possible):
• Welcome
• Featured Listings
• Previously Sold
• Sell
• Property Search
• Team
• Videos
• Blog
• Explore O.C.
• Contact

I have attached the beach and logo pics that we would like to use as the header, a few pictures of the team, and one sample home/view pic which can be used in any of the other sections (for pictures of the homes, just find expensive oceanfront houses and that will be fine).

I promise to provide feedback to each and every design submission. I appreciate the hard work that all of you are putting into your designs. There can be only one contest winner, but I hope to give all of you helpful feedback to submit the best designs possible!

Target Market(s)

Very wealthy home owners of oceanfront properties. These properties are worth several millions of dollars, and thus the site and brand needs to be targeted to very wealthy, successful individuals and families (both US and international buyers).

Industry/Entity Type

Real Estate

Number of Pages Required

2 page

Requirements
Must have
• I don’t want to give too many requirements, because I want to let you all be creative. However, here are the few Must Haves:
• Must submit 2 page designs (a home page and a sub page)
• Must use logo provided
• Focus is mostly on homes, but I would like to include some beach/ocean imagery as well
• The first “item” on the home page should be an accordion/slider which shows pictures of homes and with 1 line of text: “List with the Leader” and two link buttons: “Sell Your Home” and “Buy Your Home”
• Color palette needs to be mainly blues--to match ocean and sky blue
• Exported in all major formats (psd,ai,eps,png,jpeg,etc)
Nice to have
• We don’t necessarily need all of these, but would like to feature most:
• List of videos
• “Meet the Team”—brief team bios and pics
• Link(s) to Blog
• “List with the Leader” – section on why they should choose this firm
• Featured Listings
• Previously Sold

```html
<!DOCTYPE html>
<html lang="en">
<head>
<meta charset="utf-8">
<title>Marlow on the Shore — Previously Sold</title>
<link rel="stylesheet" href="https://fonts.googleapis.com/css2?family=Fredoka:wght@500;600;700&display=swap">
<style>
  :root {
    --charcoal: #3a3b40;
    --charcoal-dark: #323338;
    --white: #ffffff;
    --accent-blue: #2a8be0;
    --sold-red: #e23a3a;
    --ink: #2b3442;
    --logo-grey: #cfcfcf;
    --logo-ink: #5b5b5b;
    --frame-white: rgba(255, 255, 255, 0.45);
  }
  * { box-sizing: border-box; margin: 0; padding: 0; }
  html, body { width: 1200px; height: 675px; overflow: hidden; }
  body {
    position: relative;
    font-family: "Fredoka", sans-serif;
    background: var(--charcoal);
  }

  /* Header */
  .site-header {
    position: absolute; left: 0; top: 0; width: 1200px; height: 77px;
    background: var(--charcoal);
  }
  .brand {
    position: absolute; left: 25px; top: 12px; width: 76px; height: 53px;
    background: var(--logo-grey);
    display: flex; align-items: center; justify-content: center; text-align: center;
    color: var(--logo-ink); font-weight: 500; font-size: 12px; line-height: 1.15;
    text-transform: uppercase; letter-spacing: 0.5px;
  }
  .main-nav {
    position: absolute; left: 129px; top: 28px; width: 794px;
    display: flex; justify-content: space-between; white-space: nowrap;
  }
  .main-nav a {
    color: var(--white); text-decoration: none; text-transform: uppercase;
    font-weight: 600; font-size: 15.6px; letter-spacing: -0.3px; line-height: 22px;
  }
  .main-nav a.is-current { color: var(--accent-blue); }
  .cta {
    position: absolute; top: 16px; width: 97px; height: 44px;
    background: var(--accent-blue); border-radius: 5px;
    color: var(--white); font-weight: 600; font-size: 17px;
    display: flex; align-items: center; justify-content: center;
    text-decoration: none; text-transform: uppercase;
  }
  .cta-sell { left: 955px; }
  .cta-buy { left: 1074px; }

  /* Hero photo area */
  .listing-stage {
    position: absolute; left: 0; top: 77px; width: 1200px; height: 546px;
    overflow: hidden;
  }
  .stage-backdrop {
    position: absolute; inset: 0;
    background:
      linear-gradient(180deg, rgba(130,160,220,0.9) 0%, rgba(170,190,215,0.7) 25%, rgba(190,180,150,0.6) 50%, rgba(120,200,170,0.75) 75%, rgba(70,150,160,0.85) 100%),
      linear-gradient(90deg, #c9b79a 0%, #8fb0c8 50%, #6aa89a 100%);
  }
  .stage-veil {
    position: absolute; inset: 0;
    background: linear-gradient(90deg, rgba(255,255,255,0.25) 0%, rgba(255,255,255,0.35) 50%, rgba(255,255,255,0.3) 100%);
  }

  /* Listing card */
  .listing-frame {
    position: absolute; left: 113px; top: 21px; width: 386px; height: 500px;
    background: var(--frame-white);
  }
  .listing-photo {
    position: absolute; left: 131px; top: 35px; width: 352px; height: 352px;
    background:
      linear-gradient(180deg, #2c4fb8 0%, #6d7fb9 22%, #c89a5a 45%, #6f7a5e 60%, #3fcfae 78%, #1b7c8a 100%);
  }
  .listing-info {
    position: absolute; left: 131px; top: 387px; width: 352px; height: 117px;
    background: var(--charcoal);
    color: var(--white);
  }
  .status {
    position: absolute; left: 26px; top: 7px;
    color: var(--sold-red); font-weight: 600; font-size: 11px; text-transform: uppercase;
  }
  .price {
    position: absolute; left: 26px; top: 25px;
    font-weight: 600; font-size: 11.5px; text-transform: uppercase;
  }
  .location {
    position: absolute; left: 26px; top: 48px;
    display: flex; align-items: center; gap: 3px;
    font-weight: 600; font-size: 7.5px; text-transform: uppercase;
  }
  .contact-btn {
    position: absolute; left: 263px; top: 18px; width: 66px; height: 24px;
    background: var(--accent-blue); border-radius: 4px;
    display: flex; align-items: center; justify-content: center;
    color: var(--white); font-weight: 600; font-size: 10.5px; text-transform: uppercase; text-decoration: none;
  }
  .agent-avatar {
    position: absolute; left: 27px; top: 74px; width: 35px; height: 35px;
    border-radius: 50%; border: 2px solid #9a9a9a;
    background: linear-gradient(160deg, #8c7a6a, #4a4d57);
  }
  .agent-details {
    position: absolute; left: 73px; top: 78px;
    font-weight: 600; font-size: 7.5px; line-height: 16px; text-transform: uppercase;
  }
  .social-links {
    position: absolute; left: 264px; top: 81px;
    display: flex; gap: 8px;
  }
  .social-dot {
    width: 17px; height: 17px; border-radius: 50%; background: var(--white);
  }

  /* Description */
  .description {
    position: absolute; left: 629px; top: 22px; width: 526px; height: 500px;
    overflow: hidden; color: var(--ink);
  }
  .description h1 {
    font-weight: 700; font-size: 26.5px; letter-spacing: 0; text-transform: uppercase;
    line-height: 34px; margin-bottom: 6px; white-space: nowrap;
  }
  .description p {
    font-weight: 600; font-size: 10.4px; line-height: 28.6px;
    text-transform: uppercase; text-align: justify;
  }

  .site-footer {
    position: absolute; left: 0; top: 623px; width: 1200px; height: 52px;
    background: var(--charcoal-dark);
  }
</style>
</head>
<body>
  <header class="site-header">
    <div class="brand">Marlow<br>on the<br>Shore</div>
    <nav class="main-nav">
      <a href="#">Welcome</a>
      <a href="#">Featured Listings</a>
      <a href="#" class="is-current">Previously Sold</a>
      <a href="#">Team</a>
      <a href="#">Videos</a>
      <a href="#">Blog</a>
      <a href="#">Explore O.C.</a>
      <a href="#">Contact</a>
    </nav>
    <a href="#" class="cta cta-sell">Sell</a>
    <a href="#" class="cta cta-buy">Buy</a>
  </header>

  <main class="listing-stage">
    <div class="stage-backdrop" role="img" aria-label="Faded photo of a luxury oceanfront home with a curving lit pool and palm trees"></div>
    <div class="stage-veil"></div>

    <div class="listing-frame"></div>
    <div class="listing-photo" role="img" aria-label="Photo of a modern luxury home at dusk with a glowing turquoise pool and palms"></div>

    <section class="listing-info">
      <span class="status">Sold</span>
      <span class="price">$ 3 Million</span>
      <span class="location">
        <svg width="8" height="11" viewBox="0 0 8 11" aria-hidden="true"><path d="M4 0a4 4 0 0 1 4 4c0 3-4 7-4 7S0 7 0 4a4 4 0 0 1 4-4z" fill="#2a8be0"/><circle cx="4" cy="4" r="1.5" fill="#fff"/></svg>
        Beverly Hills, California
      </span>
      <a href="#" class="contact-btn">Contact</a>
      <div class="agent-avatar" role="img" aria-label="Agent portrait"></div>
      <div class="agent-details">Contact Ellis<br>Phone: 1.800.55510</div>
      <div class="social-links">
        <span class="social-dot"></span>
        <span class="social-dot"></span>
        <span class="social-dot"></span>
      </div>
    </section>

    <article class="description">
      <h1>Detailed Description</h1>
      <p>Lorem ipsum dolor sit amet, consectetur adipiscing elit. Duis congue tincidunt leo, id consectetur risus ullamcorper vel. Praesent in ultrices urna. Curabitur nec ipsum nec odio blandit bibendum. In ac nibh congue nunc pharetra facilisis. Suspendisse eget neque justo. Sed at finibus velit, id egestas diam. Vivamus nibh ante, ultrices id dignissim vitae, feugiat quis massa. Pellentesque vitae nisl et dui fringilla imperdiet. Aliquam erat volutpat. Nullam mollis non lacus id convallis. Vivamus gravida nulla ac bibendum dictum. Praesent lobortis sollicitudin nisi, nec pharetra dolor tristique vel. Donec maximus erat et est porttitor fermentum. Nunc non ex molestie, malesuada mauris non, dignissim ipsum.</p>
      <p>Vestibulum blandit pretium odio, sed ultrices arcu aliquet vel. Donec elementum bibendum nisl, eget sollicitudin ligula commodo maximus. Curabitur varius lobortis pulvinar. Ut iaculis nunc augue, ut mollis sem convallis sed. Nulla vestibulum euismod diam, non posuere felis bibendum vel. Donec auctor urna nulla, et convallis magna blandit ac. Vivamus rutrum egestas nibh sit amet porttitor. Vestibulum eu vulputate est.</p>
      <p>Proin blandit lacinia turpis eu pulvinar. Ut non tortor eu velit condimentum tempus ac id turpis. Ut laoreet magna quis felis bibendum, in pretium purus tincidunt. Nam laoreet interdum dolor. Donec gravida tortor at interdum viverra. Morbi dui diam, rhoncus at mauris in.</p>
    </article>
  </main>

  <footer class="site-footer"></footer>
</body>
</html>
```